Handout for attendees of educational seminar

I provide educational workshops on how to give technical presentations at conferences to scientists and engineers. My company is called Craft Talk Studio (www.CraftTalkStudio.example). I would like a double sided, half page size flyer that can be used as a handout for attendees of my workshops. On one side of the flyer, they will get top tips for creating their next presentation. On the other side, they will get my photo, bio, and contact information. I have uploaded a draft of a full page design I made myself. I'd like the copy of the tips to remain the same, but everything else is flexible.

Target Market(s)

scientists, engineers, technical professionals

Font styles to use
Serif
Sans Serif

Requirements
Must have
• my photo (I've provided two options to choose from depending on colors...photo on side 2 only), my logo, flyer needs to be half page in size (5.5" x 8.5"), needs to be double sided, One side has the "tips" and the other side has my personal details (see attached page for copy).
Nice to have
• I like the use of icons on the "tips" side of the flyer.

```html
<!DOCTYPE html>
<html lang="en">
<head>
<meta charset="utf-8">
<title>Craft Talk Studio – Quick Tips Handout</title>
<link rel="stylesheet" href="https://fonts.googleapis.com/css2?family=Oswald:wght@300;400&family=Poppins:wght@400;600;700&display=swap">
<style>
  :root{
    --stage:#8d8e91;
    --stage-light:#a4a5a8;
    --charcoal:#4f4f51;
    --charcoal-dark:#3d3d3f;
    --slate:#5c5c5e;
    --green:#8db36a;
    --green-deep:#6f9a4c;
    --ink:#1f1f1f;
    --paper:#ffffff;
    --sans:'Poppins', Arial, sans-serif;
    --display:'Oswald', 'Arial Narrow', sans-serif;
  }
  *{box-sizing:border-box;margin:0;padding:0}
  html,body{width:1200px;height:1200px;overflow:hidden}
  body{background:radial-gradient(ellipse at 50% 45%, var(--stage-light), var(--stage) 75%);font-family:var(--sans);color:var(--ink);position:relative}
  .flyer{position:absolute;top:262px;width:426px;height:656px;background:var(--paper);overflow:hidden;box-shadow:8px 12px 22px rgba(0,0,0,.35)}
  .flyer--tips{left:116px}
  .flyer--about{left:642px}
  .abs{position:absolute}

  .backdrop{left:0;right:0;bottom:30px;height:230px;background:linear-gradient(to bottom, rgba(235,235,235,0), rgba(228,228,228,.7))}

  /* tips header */
  .tips-header{left:0;top:0;width:426px;height:148px}
  .brand-kicker{left:48px;top:52px;font-family:var(--display);font-weight:300;font-size:14px;color:#fff;letter-spacing:.3px;font-variant:small-caps}
  .brand-rule{left:48px;width:162px;height:1px;background:#dcdcdc}
  .title{left:46px;top:68px;font-family:var(--display);font-weight:300;font-size:44px;line-height:1;color:#fff;letter-spacing:.5px}
  .motto{left:48px;top:119px;font-family:var(--display);font-weight:300;font-size:7.6px;color:#e6e6e6;letter-spacing:-.1px}
  .badge-name{font-family:var(--sans);font-weight:600;color:var(--green);text-align:center}

  /* tips body */
  .pill{height:18px;padding:0 14px;border-radius:9px;background:var(--slate);color:#fff;font-weight:700;font-size:8.6px;line-height:18px;box-shadow:1px 2px 3px rgba(0,0,0,.3)}
  .icon{width:50px;height:50px;border-radius:50%;background:var(--charcoal);display:flex;align-items:center;justify-content:center}
  .tip-text{width:298px;font-size:9px;line-height:11.6px;text-align:justify}
  .tip-rule{height:1px;background:linear-gradient(to right, var(--charcoal), #bdbdbd)}
  .hl{color:var(--green-deep);font-weight:600}
  .cta{left:88px;top:545px;width:246px;height:48px;background:var(--charcoal);border-radius:5px;color:#fff;font-weight:700;font-size:9px;line-height:11.6px;text-align:center;padding-top:7px;box-shadow:1px 3px 5px rgba(0,0,0,.35)}
  .sign-name{font-family:var(--sans);color:var(--green);font-weight:400;text-align:center}
  .sign-tag{color:var(--green-deep);letter-spacing:3px;text-align:center}

  /* footer */
  .footer{left:0;bottom:0;width:426px;height:30px;background:linear-gradient(to right, var(--charcoal-dark) 0%, var(--slate) 25%, var(--green) 55%, var(--slate) 80%, var(--charcoal-dark) 100%)}
  .footer-text{bottom:6px;font-size:10px;line-height:12px;color:#fff}
  .footer-icon{width:26px;height:26px;border-radius:50%;background:var(--charcoal);border:2px solid #fff;top:604px;display:flex;align-items:center;justify-content:center}

  /* about side */
  .stage-photo{left:0;top:0;width:426px;height:140px;background:linear-gradient(to bottom, rgba(255,255,255,0) 55%, #fff 100%), linear-gradient(100deg, #2d1c4a 0%, #5a2a5e 40%, #8a2a4a 65%, #3a2a5e 100%)}
  .meet{right:34px;top:83px;font-family:var(--display);font-weight:400;font-size:27px;color:#fff;letter-spacing:.2px}
  .portrait{left:308px;top:114px;width:84px;height:84px;border-radius:50%;background:radial-gradient(circle at 50% 40%, #d9b48e, #8a5a3a 60%, #1f7a4a 100%);border:2px solid #fff}
  .bio{left:34px;top:162px;width:358px;font-size:10.4px;line-height:12.8px;text-align:justify}
  .bio p{text-indent:21px;margin-bottom:8.5px}
  .portrait-space{float:right;width:86px;height:38px}
  .seal{left:182px;top:490px;width:60px;height:60px;border-radius:50%;background:var(--charcoal)}
  .slogan{left:0;width:426px;top:606px;font-size:7.6px;color:#9a9a9a;text-align:center;font-weight:400}
</style>
</head>
<body>

<!-- Side 1: tips -->
<section class="flyer flyer--tips">
  <svg class="abs tips-header" viewBox="0 0 426 148" aria-hidden="true">
    <rect width="426" height="148" fill="#5c5c5e"/>
    <polygon points="250,148 426,20 426,148" fill="#4a4a4c"/>
    <circle cx="348" cy="54" r="96" fill="#fff"/>
    <circle cx="348" cy="54" r="90" fill="#4f4f51"/>
    <rect x="200" y="148" width="226" height="10" fill="#fff"/>
  </svg>
  <div class="abs badge-name" style="left:296px;top:44px;width:110px;font-size:13px;line-height:15px">Craft Talk<br>Studio</div>

  <div class="abs brand-kicker">Craft Talk Studio</div>
  <div class="abs brand-rule" style="top:69px"></div>
  <div class="abs title">QUICK TIPS</div>
  <div class="abs brand-rule" style="top:115px"></div>
  <div class="abs motto">SCIENCE NOT COMMUNICATED IS SCIENCE NOT DONE!</div>

  <!-- Tip 1 -->
  <div class="abs pill" style="left:34px;top:171px">Be Audience Centered</div>
  <div class="abs icon" style="left:33px;top:203px">
    <svg width="30" height="30" viewBox="0 0 30 30" aria-hidden="true" fill="#fff">
      <circle cx="8" cy="10" r="3.5"/><circle cx="22" cy="10" r="3.5"/><circle cx="15" cy="8" r="4"/>
      <path d="M2 24c0-5 3-8 6-8s6 3 6 8zM16 24c0-5 3-8 6-8s6 3 6 8z"/>
      <path d="M8 26c0-6 3-9 7-9s7 3 7 9z"/>
    </svg>
  </div>
  <p class="abs tip-text" style="left:96px;top:202px">Your ability to be successful as a speaker depends upon your ability to make your audience successful.</p>
  <div class="abs tip-rule" style="left:96px;top:230px;width:298px"></div>
  <p class="abs tip-text" style="left:96px;top:236px">TIP: Return to <span class="hl">"Points of Common Ground"</span> throughout the talk that answer the question <span class="hl">"So what?"</span> about the scientific info. Be an interpreter!</p>

  <!-- Tip 2 -->
  <div class="abs pill" style="left:34px;top:290px">Filter &amp; Focus</div>
  <div class="abs icon" style="left:33px;top:321px">
    <svg width="28" height="28" viewBox="0 0 28 28" aria-hidden="true"><path d="M3 4h22l-8 10v10l-6-3v-7z" fill="none" stroke="#8db36a" stroke-width="2" stroke-linejoin="round"/></svg>
  </div>
  <p class="abs tip-text" style="left:98px;top:320px">When you try to share everything, you share nothing.</p>
  <div class="abs tip-rule" style="left:98px;top:337px;width:296px"></div>
  <p class="abs tip-text" style="left:98px;top:343px;width:296px">TIP: Start your planning with the <span class="hl">"view"</span> you want your audience to have at the end of the talk. Then ask yourself <span class="hl">"What would they need to know in order to get there?"</span></p>

  <!-- Tip 3 -->
  <div class="abs pill" style="left:34px;top:398px">Show Your Science</div>
  <div class="abs icon" style="left:33px;top:428px">
    <svg width="30" height="30" viewBox="0 0 30 30" aria-hidden="true" fill="none" stroke="#fff" stroke-width="1.4">
      <ellipse cx="15" cy="15" rx="12" ry="4.5"/>
      <ellipse cx="15" cy="15" rx="12" ry="4.5" transform="rotate(60 15 15)"/>
      <ellipse cx="15" cy="15" rx="12" ry="4.5" transform="rotate(-60 15 15)"/>
      <circle cx="15" cy="15" r="2.4" fill="#8db36a" stroke="none"/>
    </svg>
  </div>
  <p class="abs tip-text" style="left:98px;top:428px;width:296px">Your slides should do something for you that your words cannot. This means make your slides <span class="hl">Visual not Verbal</span>.</p>
  <div class="abs tip-rule" style="left:98px;top:457px;width:296px"></div>
  <p class="abs tip-text" style="left:98px;top:463px;width:296px;text-align:left">TIP: <span class="hl">No Bullet Points</span> (seriously!). Have a brief take-away messages supported by visual evidence.</p>

  <div class="abs backdrop" role="img" aria-label="Faint geometric backdrop"></div>

  <div class="abs cta">Need more help? Check out Dana Whitfield's<br>Craft Talk Studio Boot Camp<br>training program. Includes 1:1 Coaching!</div>

  <div class="abs sign-name" style="left:0;width:426px;top:599px;font-size:14px;line-height:16px">Dana Whitfield</div>
  <div class="abs sign-tag" style="left:0;width:426px;top:614px;font-size:5px">Craft Talk Studio</div>

  <div class="abs footer"></div>
  <div class="abs footer-icon" style="left:50px">
    <svg width="13" height="10" viewBox="0 0 13 10" aria-hidden="true"><rect x=".5" y=".5" width="12" height="9" fill="#fff"/><path d="M.5 .5l6 5 6-5" fill="none" stroke="#4f4f51"/></svg>
  </div>
  <div class="abs footer-icon" style="left:349px">
    <svg width="14" height="14" viewBox="0 0 14 14" aria-hidden="true" fill="none" stroke="#fff" stroke-width="1.1"><circle cx="7" cy="7" r="6"/><ellipse cx="7" cy="7" rx="2.6" ry="6"/><path d="M1 7h12M2 4h10M2 10h10"/></svg>
  </div>
  <div class="abs footer-text" style="left:17px">dana@crafttalkstudio.example</div>
  <div class="abs footer-text" style="right:26px">www.CraftTalkStudio.example</div>
</section>

<!-- Side 2: about -->
<section class="flyer flyer--about">
  <div class="abs stage-photo" role="img" aria-label="Photo of Dana speaking on a conference stage"></div>
  <div class="abs meet">MEET DANA</div>

  <div class="abs bio">
    <div class="portrait-space"></div>
    <p>Dana Whitfield is on a mission: to transform how scientists, engineers, and technical professionals present their work. That's because she believes that even the best technical ideas are destined to remain undiscovered unless presented in a clear and compelling way that sparks innovation and drives adoption.</p>
    <p>For a decade, she's traveled around the world to work with Global 100 corporations, institutions and universities, teaching the proven strategies she's mastered through her consulting work and during her time as a faculty member Northfield State University.</p>
    <p>Dana is internationally known for her popular Open Stage talk entitled "Speak Plainly to Me" which has over 2 million views (and counting!).</p>
    <p>Teams that work with Dana get the practical skills and natural confidence they need to immediately shift their "information dump"-style presentations into ones that are meaningful, engaging, and inspire people to take action.</p>
    <p>Dana provides on-site group workshops and coaching, conference sessions and keynotes, and 1:1 consultation.</p>
  </div>
  <div class="abs portrait" role="img" aria-label="Portrait photo of Dana Whitfield"></div>

  <div class="abs backdrop" role="img" aria-label="Faint geometric backdrop"></div>

  <div class="abs seal"></div>
  <div class="abs sign-name" style="left:0;width:426px;top:554px;font-size:19px;line-height:22px">Dana Whitfield</div>
  <div class="abs sign-tag" style="left:0;width:426px;top:576px;font-size:6.5px">Craft Talk Studio</div>
  <div class="abs slogan">SCIENCE NOT COMMUNICATED IS SCIENCE NOT DONE</div>

  <div class="abs footer"></div>
  <div class="abs footer-icon" style="left:50px">
    <svg width="13" height="10" viewBox="0 0 13 10" aria-hidden="true"><rect x=".5" y=".5" width="12" height="9" fill="#fff"/><path d="M.5 .5l6 5 6-5" fill="none" stroke="#4f4f51"/></svg>
  </div>
  <div class="abs footer-icon" style="left:349px">
    <svg width="14" height="14" viewBox="0 0 14 14" aria-hidden="true" fill="none" stroke="#fff" stroke-width="1.1"><circle cx="7" cy="7" r="6"/><ellipse cx="7" cy="7" rx="2.6" ry="6"/><path d="M1 7h12M2 4h10M2 10h10"/></svg>
  </div>
  <div class="abs footer-text" style="left:17px">dana@crafttalkstudio.example</div>
  <div class="abs footer-text" style="right:26px">www.CraftTalkStudio.example</div>
</section>

</body>
</html>
```